Software Company Business Card Design

We are looking for a business card design for a software, messaging & IT services company based in Australia.

Talvora Group is the holding company for 3 brands all offering technology based business solutions; Talvora, Brindle & Quillpad. Brand Identity = Friendly, Professional, Viable, Vibrant, Creative

We want our business card to reflect that we are an innovative market leader. The design should be clean, professional and original.

This design will be used for all 3 brands.

More information about our company can be found at: www.talvoragroup.example.au
www.brindle.example.au

Details we would like on the card:

Firstname Lastname
Position
Level 17, 482 Ormond Rd
East Harlow
VIC 3999
Phone: +61 2 5550 1738
Fax: +61 2 5550 1794
Mobile:
Email:
www.talvoragroup.example.au

Target Market(s)

Our business cards are given to B2B and industry professionals.

Industry/Entity Type

Business

Requirements
Must have
• The Business Card must include the same colours as the logo.
Nice to have
• We would like it to me double sided.

```html
<!DOCTYPE html>
<html lang="en">
<head>
<meta charset="utf-8">
<title>Talvora Group – Business Card</title>
<link href="https://fonts.googleapis.com/css2?family=Arimo:wght@400;700&display=swap" rel="stylesheet">
<style>
  :root {
    --brand-crimson: #b0103e;
    --ink: #111111;
    --paper: #ffffff;
  }
  html, body {
    margin: 0;
    padding: 0;
    width: 1200px;
    height: 732px;
    overflow: hidden;
    background: var(--paper);
  }
  .card {
    position: relative;
    width: 1200px;
    height: 732px;
    background: var(--paper);
    font-family: "Arimo", Arial, sans-serif;
    color: var(--ink);
    overflow: hidden;
  }
  .wordmark {
    position: absolute;
    left: 22px;
    top: 4px;
    width: 580px;
    color: var(--brand-crimson);
    font-weight: 700;
    line-height: 1;
  }
  .wordmark__name {
    display: block;
    font-size: 168px;
    letter-spacing: -3px;
    white-space: nowrap;
  }
  .wordmark__group {
    display: block;
    text-align: right;
    font-size: 56px;
    margin-top: 0;
    padding-right: 2px;
  }
  .identity {
    position: absolute;
    right: 28px;
    top: 72px;
    text-align: right;
    color: var(--brand-crimson);
    font-weight: 700;
    font-size: 32px;
    line-height: 48px;
  }
  .identity p { margin: 0; }
  .contact {
    position: absolute;
    right: 28px;
    top: 354px;
    text-align: right;
    font-style: normal;
    font-size: 33px;
    line-height: 47px;
  }
  .contact p { margin: 0; }
</style>
</head>
<body>
  <main class="card">
    <div class="wordmark" aria-label="Talvora Group">
      <span class="wordmark__name">Talvora</span>
      <span class="wordmark__group">Group</span>
    </div>

    <div class="identity">
      <p class="identity__name">Firstname Lastname</p>
      <p class="identity__position">Position</p>
    </div>

    <address class="contact">
      <p>Level 17, 482 Ormond Rd</p>
      <p>East Harlow</p>
      <p>VIC 3999</p>
      <p>tel: +61 2 5550 1738</p>
      <p>fax: +61 2 5550 1794</p>
      <p>mob: +61 400 555 019</p>
      <p>eml: person@talvoragroup.example.au</p>
      <p>web: www.talvoragroup.example.au</p>
    </address>
  </main>
</body>
</html>
```